Album Jacket for young indie musicians for AFRICA #1 TOLUWENDE

We are REKO SOUND (reko-sound.net), a music label for young African musicians living in a slum. I would like to ask you to design our new album's cover jacket. The title is TOLUWENDE, musician name is Dalemo. Add our label logo (we have various versions and can provide). I attached Dalemo's photo also. Please listen to the music of the album on Soundcloud. https://tunepail.example/tags/dalemo

Our another musician, Jorro was on the stage of Kenyan most popular TV program yesterday. His music video is so nice. If you have a time, please look at it. https://www.clipvane.example/watch?v=Q8R__kD2Lp4&feature=clipvane.example

Target Market(s)

International. not only African funs.

Font styles to use
Decorative

Requirements
Must have
• Title, Musician's name, REKO SOUND Logo

```html
<!DOCTYPE html>
<html lang="en">
<head>
<meta charset="utf-8">
<title>TOLUWENDE · Dalemo · Album Cover</title>
<link rel="stylesheet" href="https://fonts.googleapis.com/css2?family=Monoton&family=Montserrat:wght@300;800&display=swap">
<style>
  :root {
    --taupe: #a29c93;
    --white: #ffffff;
    --mauve: #6f4b57;
    --rose: #e2405f;
    --label-band: rgba(112, 104, 99, 0.55);
    --ink: #2a2426;
  }
  html, body {
    margin: 0;
    padding: 0;
    overflow: hidden;
    background: var(--taupe);
  }
  .cover {
    position: relative;
    width: 1200px;
    height: 1151px;
    background: var(--taupe);
    overflow: hidden;
  }
  .portrait {
    position: absolute;
    left: 230px;
    top: 150px;
    width: 960px;
    height: 936px;
    background: linear-gradient(180deg, var(--mauve) 0%, var(--mauve) 55%, var(--rose) 100%);
    border-radius: 46% 46% 0 0 / 30% 30% 0 0;
  }
  .rule {
    position: absolute;
    left: 0;
    width: 1200px;
    height: 5px;
    background: var(--white);
  }
  .rule--top { top: 66px; }
  .rule--bottom { top: 1086px; }
  .headline {
    position: absolute;
    left: 0;
    top: 0;
    width: 1200px;
    height: 340px;
  }
  .album-title {
    font-family: 'Monoton', 'Montserrat', sans-serif;
    font-size: 150px;
    fill: var(--white);
  }
  .artist-name {
    font-family: 'Montserrat', sans-serif;
    font-weight: 300;
    font-size: 48px;
    fill: var(--white);
  }
  .label-band {
    position: absolute;
    left: 668px;
    top: 939px;
    width: 532px;
    height: 110px;
    background: var(--label-band);
    display: flex;
    align-items: center;
    gap: 22px;
    padding-left: 22px;
    box-sizing: border-box;
    color: var(--ink);
    font-family: 'Montserrat', sans-serif;
  }
  .label-square {
    flex: none;
    width: 58px;
    height: 58px;
    background: var(--ink);
  }
  .label-text {
    display: flex;
    flex-direction: column;
  }
  .label-name {
    font-weight: 800;
    font-size: 52px;
    line-height: 1;
    letter-spacing: 0.5px;
  }
  .label-tagline {
    margin-top: 8px;
    font-weight: 300;
    font-size: 20px;
    line-height: 1;
    letter-spacing: 1px;
  }
</style>
</head>
<body>
  <main class="cover">
    <div class="portrait" role="img" aria-label="Posterised portrait of the musician Dalemo in a striped red shirt against a weathered wall"></div>
    <div class="rule rule--top"></div>
    <div class="rule rule--bottom"></div>
    <svg class="headline" viewBox="0 0 1200 340" aria-label="TOLUWENDE by DALEMO">
      <text class="album-title" x="78" y="235" textLength="1046" lengthAdjust="spacingAndGlyphs">TOLUWENDE</text>
      <text class="artist-name" x="215" y="316" textLength="785" lengthAdjust="spacing">DALEMO</text>
    </svg>
    <div class="label-band">
      <span class="label-square"></span>
      <div class="label-text">
        <span class="label-name">REKO SOUND</span>
        <span class="label-tagline">new voices, one sound</span>
      </div>
    </div>
  </main>
</body>
</html>
```